Flyer Design Dental Office Grand Opening offer

Dental office.

Grand opening flyer. Offer Exam + cleaning + xrays.
special: free teeth whitening ($200 value)

Target Market(s)

Middle class people around Huntington Beach.

Industry/Entity Type

Dental Clinic

Colors
cfeae6
86cfc6
fac994
fee18a
e667a6

Requirements
Must have
• Do not change my existing logo
Nice to have
• Have some appealing picture/design to catch the eye, but not too flashy
Should not have
• No cartoon kind of design

```html
<!DOCTYPE html>
<html lang="en">
<head>
<meta charset="utf-8">
<title>Harbor Dental – Grand Opening</title>
<link rel="stylesheet" href="https://fonts.googleapis.com/css2?family=Archivo+Black&family=Arimo:ital,wght@0,400;0,700;1,700&display=swap">
<style>
  :root {
    --teal: #1c9cac;
    --teal-light: #5ec0cf;
    --aqua-pale: #cfeae6;
    --pink: #e667a6;
    --orange: #f26a2a;
    --cream: #fac994;
    --yellow-pale: #fee18a;
    --navy: #2a4f8f;
    --white: #ffffff;
  }
  html, body {
    margin: 0;
    padding: 0;
    overflow: hidden;
  }
  .flyer {
    position: relative;
    width: 933px;
    height: 1200px;
    overflow: hidden;
    font-family: "Arimo", Arial, sans-serif;
    background: linear-gradient(118deg, var(--teal-light) 0%, var(--aqua-pale) 42%, var(--white) 68%);
  }
  .backdrop {
    position: absolute;
    inset: 0;
  }
  .brand {
    position: absolute;
    left: 468px;
    top: 88px;
    display: flex;
    align-items: center;
    gap: 18px;
  }
  .brand-mark {
    width: 54px;
    height: 54px;
    background: var(--teal);
  }
  .brand-name {
    font-family: "Arimo", Arial, sans-serif;
    font-weight: 700;
    font-size: 58px;
    letter-spacing: 3px;
    color: var(--teal);
    line-height: 1;
  }
  .dentist {
    position: absolute;
    right: 76px;
    top: 201px;
    font-size: 17px;
    color: #222;
  }
  .headline {
    position: absolute;
    left: 0;
    width: 100%;
    top: 246px;
    margin: 0;
    text-align: center;
    font-family: "Archivo Black", "Arial Black", sans-serif;
    font-weight: 400;
    font-size: 72px;
    letter-spacing: 3px;
    line-height: 1;
    background: linear-gradient(180deg, #ffffff 0%, #9fb8d6 45%, #6f8fbf 100%);
    -webkit-background-clip: text;
    background-clip: text;
    color: transparent;
    -webkit-text-stroke: 2.5px var(--navy);
  }
  .phone {
    position: absolute;
    left: 0;
    width: 100%;
    top: 360px;
    text-align: center;
    font-weight: 700;
    font-size: 47px;
    color: var(--orange);
  }
  .address {
    position: absolute;
    left: 0;
    width: 100%;
    top: 424px;
    text-align: center;
    font-size: 25px;
    color: var(--orange);
  }
  .tagline {
    position: absolute;
    left: 36px;
    top: 560px;
    transform: rotate(-14deg);
    transform-origin: left top;
    font-weight: 700;
    font-style: italic;
    font-size: 48px;
    line-height: 1.08;
    letter-spacing: 2px;
    color: var(--white);
    -webkit-text-stroke: 1.2px var(--teal-light);
  }
  .price {
    position: absolute;
    left: 648px;
    top: 572px;
    font-weight: 700;
    font-size: 150px;
    line-height: 1;
    color: var(--white);
    letter-spacing: -2px;
  }
  .offer {
    position: absolute;
    left: 430px;
    top: 694px;
    font-weight: 700;
    font-size: 31px;
    line-height: 1.42;
    color: var(--white);
  }
  .whitening {
    position: absolute;
    left: 40px;
    top: 782px;
    width: 390px;
    text-align: center;
    color: var(--white);
    font-weight: 700;
  }
  .whitening-free {
    display: block;
    font-size: 92px;
    line-height: 1;
    color: var(--orange);
    -webkit-text-stroke: 2px var(--white);
  }
  .whitening-label {
    display: block;
    font-size: 44px;
    line-height: 1.35;
  }
  .whitening-note {
    position: absolute;
    left: 38px;
    top: 990px;
    font-size: 19px;
    font-weight: 700;
    color: var(--cream);
  }
  .celebration {
    position: absolute;
    left: 688px;
    top: 975px;
    font-size: 30px;
    line-height: 1.3;
    color: var(--white);
  }
  .plans {
    position: absolute;
    left: 77px;
    top: 1155px;
    font-size: 20px;
    font-weight: 700;
    color: var(--yellow-pale);
  }
</style>
</head>
<body>
<main class="flyer">
  <svg class="backdrop" width="933" height="1200" viewBox="0 0 933 1200" aria-hidden="true">
    <path class="pink-sweep" fill="var(--pink)"
      d="M933 560 C 740 560 560 600 455 690 C 330 800 180 1010 0 1175 L 0 1200 L 933 1200 Z"/>
    <path class="whitening-blob" fill="var(--teal)"
      d="M70 812 C 160 835 300 830 395 808 C 440 800 430 900 415 990 C 405 1060 320 1072 210 1066 C 110 1060 48 1050 52 960 C 55 880 40 805 70 812 Z"/>
    <path class="celebration-blob" fill="var(--teal)"
      d="M705 915 C 790 900 880 930 933 960 L 933 1200 L 700 1200 C 660 1140 640 1060 648 990 C 654 945 670 922 705 915 Z"/>
  </svg>

  <div class="brand">
    <span class="brand-mark"></span>
    <span class="brand-name">harbor dental</span>
  </div>
  <div class="dentist">Lena Park, DDS</div>

  <h1 class="headline">GRAND OPENING</h1>
  <div class="phone">(714) 555-0188</div>
  <div class="address">2280 Coral Ave., Huntington Beach, CA 92649</div>

  <div class="tagline">MAKE YOUR<br>SMILE BRIGHTER</div>

  <div class="price">$50</div>
  <div class="offer">Dental Exam<br>with X-ray and Professional<br>Cleaning (regular)</div>

  <div class="whitening">
    <span class="whitening-free">FREE</span>
    <span class="whitening-label">TEETH</span>
    <span class="whitening-label">WHITENING</span>
  </div>
  <div class="whitening-note">(after completion of dental treatment)</div>

  <div class="celebration">JOIN US FOR<br>OUR GRAND<br>OPENING<br>CELEBRATION!</div>

  <div class="plans">We welcome PPO, HMO, Denti-Cal beneficiaries</div>
</main>
</body>
</html>
```